Front and back cover design for skincare marketing materials

Thank you for showing an interest in my project.
Project Details.

I require a front and back cover for our marketing materials.
·       Front Cover size: 105 mm W x 150 mm H.
·       Back Cover size:  105 mm W x 150 mm H.
·       It must include these two colors. You can use a third color if you wish.
1.     #DBA09D
2.     #FFFFFF
 
Front Cover
·      The front cover will have a faded image of the Kakadu Plum branch and fruit. There are two image files, KP_image-1.jpg and kp_image-2.jpeg. You can use both images, just a portion of them, or source alternative royalty-free images of Kakadu Plum that may better fit the design. These two files have been uploaded.
 
The front cover wording.
Top of the front cover.
a.     The title of the image. “Kakadu Plum”
b.     The brand name, “Velora Skincare”. The file brand_name.ai uploaded.
 
Bottom of the front cover- Designer's choice of font.
The bottom of the front cover contains three lines of text in the following order.  
1.     Australian Native Ingredients
2.     100% Natural · Organic · Wild-harvested
3.     Australian-Made Premium Skincare
 
Back Cover
·      Back Cover wording.The back cover contains the following words "grown by nature" in white (#FFFFFF) of font Italianno (font_file.ttf) with a background color of #DBA09D as seen in the sample box (sample_box.pdf) right-side panel
 
Please provide one file for the front cover and a separate file for the back cover.
All the elements of the files must be editable.
 
Do NOT use the Curve function on the files, as the text must remain editable/changeable.
 
All assets/resources/files, including fonts not supplied by us but used by the designer, must be named and provided with the finished design.
Updates

Slow to provide project details.

Target Market(s)

Beauty-minded Asian consumers between the ages of 32 and 75 who take a proactive approach to maintaining younger-looking skin. Those who already know the danger of skin damage caused by skincare containing harsh chemicals choose effective natural/organic solutions to meet their skincare needs. Those who wish a more radiant glow and youthful appearance to their skin. Usually, a two-income middle to high-income bracket couples with a mindset for health and beauty.

Industry/Entity Type

beauty

Font styles to use
Other font styles liked:
• I will provide a font file and a brand name file.

Requirements
Must have
• You must use the two colors provided on the product box. The designer may use a third color.
Nice to have
• some gold colour

```html
<!DOCTYPE html>
<html lang="en">
<head>
<meta charset="utf-8">
<title>Velora Skincare – Kakadu Plum Cover</title>
<link rel="stylesheet" href="https://fonts.googleapis.com/css2?family=Italianno&family=Poppins:wght@400&family=Josefin+Sans:wght@300&display=swap">
<style>
  :root {
    --rose: #DBA09D;
    --white: #FFFFFF;
    --ink: #3E3E40;
    --page: #FFFFFF;
    --leaf-light: #EEF0D2;
    --leaf-mid: #B9CC5A;
    --leaf-deep: #5E8A2E;
    --leaf-dark: #1F3A1F;
  }
  * { margin: 0; padding: 0; box-sizing: border-box; }
  html, body {
    width: 1200px; height: 893px; overflow: hidden;
    background: var(--page);
  }
  .spread { position: relative; width: 1200px; height: 893px; }

  .cover {
    position: absolute; top: 64px;
    width: 535px; height: 765px;
    overflow: hidden;
    box-shadow: 0 2px 8px rgba(0,0,0,0.12);
  }
  .cover--front { left: 51px; }
  .cover--back { left: 614px; background: var(--rose); }

  .front-photo {
    position: absolute; inset: 0;
    background:
      radial-gradient(ellipse 45% 35% at 62% 38%, var(--leaf-light) 0%, rgba(238,240,210,0) 100%),
      radial-gradient(ellipse 40% 30% at 30% 75%, #C9B85A 0%, rgba(201,184,90,0) 100%),
      radial-gradient(ellipse 35% 40% at 95% 85%, var(--leaf-dark) 0%, rgba(31,58,31,0) 100%),
      radial-gradient(ellipse 40% 25% at 10% 100%, var(--leaf-dark) 0%, rgba(31,58,31,0) 100%),
      linear-gradient(160deg, var(--leaf-mid) 0%, #DDE3A8 35%, #A9C24E 65%, var(--leaf-deep) 100%);
  }

  .brand-name {
    position: absolute; left: 0; right: 0; top: 120px;
    text-align: center;
    font-family: "Poppins", sans-serif;
    font-weight: 400;
    font-size: 40px; line-height: 1.2;
    color: var(--ink);
  }

  .product-box {
    position: absolute; left: 166px; top: 344px;
    width: 202px; height: 75px;
    border: 1.5px solid var(--ink);
    font-family: "Josefin Sans", sans-serif;
    font-weight: 300;
    color: var(--ink);
    text-align: center;
    font-size: 31px; line-height: 31px;
    letter-spacing: 0.3em;
    padding: 8px 0 0 0.3em;
  }

  .claims {
    position: absolute; left: 0; right: 0; top: 621px;
    text-align: center;
    font-family: "Poppins", sans-serif;
    font-size: 18px; line-height: 29px;
    color: var(--white);
  }

  .tagline {
    position: absolute; left: 50%; top: 50%;
    transform: translate(-50%, -50%) rotate(-90deg);
    white-space: nowrap;
    font-family: "Italianno", cursive;
    font-size: 108px; line-height: 1;
    color: var(--white);
  }
</style>
</head>
<body>
  <main class="spread">
    <section class="cover cover--front">
      <div class="front-photo" role="img" aria-label="Softly faded photograph of a Kakadu plum branch with green fruit and leaves"></div>
      <h1 class="brand-name">Velora Skincare</h1>
      <div class="product-box">KAKADU<br>PLUM</div>
      <div class="claims">
        <p>Australian Native Ingredients</p>
        <p>100% Natural · Organic · Wild-harvested</p>
        <p>Australian-Made Premium Skincare</p>
      </div>
    </section>

    <section class="cover cover--back">
      <p class="tagline">grown by nature</p>
    </section>
  </main>
</body>
</html>
```